Veltrona5 website

Need to create a website for my business

Target Market(s)

Food ingredient companies, B2B

Industry/Entity Type

Food technology, food ingredients

Coding

Coded - Design and coding required

Number of Pages Required

2 page

Requirements
Nice to have
• Case studies, links to articles,

```html
<!DOCTYPE html>
<html lang="en">
<head>
<meta charset="utf-8">
<title>Veltrona5 — Food Technology</title>
<link rel="stylesheet" href="https://fonts.googleapis.com/css2?family=Open+Sans:wght@400;600;700&family=Ubuntu:wght@400;500;700&family=Roboto:wght@400;500&display=swap">
<style>
:root{
  --green:#138a13;
  --green-dark:#0e7410;
  --ink:#222;
  --text:#333;
  --muted:#666;
  --white:#fff;
  --footer:#262626;
  --hero-a:#8d8a85;
  --hero-b:#d9dbd8;
}
*{margin:0;padding:0;box-sizing:border-box}
html,body{width:1200px;height:3692px;overflow:hidden}
body{position:relative;font-family:"Open Sans",sans-serif;color:var(--text);background:var(--white)}
.abs{position:absolute}
.photo{position:absolute}
.btn{position:absolute;display:flex;align-items:center;justify-content:center;background:var(--green);color:var(--white);font-weight:600;text-decoration:none;clip-path:polygon(6% 0,100% 0,94% 100%,0 100%)}
.btn-light{background:var(--white);color:var(--ink)}

/* header */
.brand{position:absolute;display:flex;align-items:center;gap:12px}
.brand-dot{width:26px;height:26px;border-radius:50%;background:var(--green)}
.brand-name{font-family:"Open Sans",sans-serif;font-size:26px;font-weight:600;color:#333}
.nav{position:absolute;top:45px;left:394px;display:flex;font-size:15px;color:#222}
.nav a{color:inherit;text-decoration:none;position:absolute;white-space:nowrap}
.nav a.active{color:var(--green)}
.phone{position:absolute;left:979px;top:46px;font-size:14px;color:#222;display:flex;align-items:center;gap:8px;font-weight:600}

/* hero */
.hero{position:absolute;top:95px;left:0;width:1200px;height:484px;background:linear-gradient(90deg,var(--hero-a) 0%,#b8b7b2 45%,var(--hero-b) 100%)}
.hero-shade{position:absolute;inset:0;background:linear-gradient(90deg,rgba(0,0,0,.45),rgba(0,0,0,0) 60%)}
.hero-title{left:100px;top:96px;font-size:37px;color:var(--white);font-weight:400}
.hero-title b{font-weight:700}
.hero-text{left:100px;top:156px;width:420px;font-size:17.5px;line-height:30px;color:var(--white)}
.follow{left:100px;top:434px;display:flex;align-items:center;color:var(--white);font-size:15px}
.follow .rule{width:100px;height:1px;background:rgba(255,255,255,.8);margin:0 26px 0 12px}
.follow .soc{width:12px;height:12px;border-radius:50%;background:var(--white);margin-right:34px}

/* about */
.about-kicker{left:508px;top:676px;font-size:21px;font-weight:600;color:#333}
.about-title{left:506px;top:704px;font-size:34px;font-weight:700;color:var(--green);font-family:"Ubuntu",sans-serif}
.about-text{left:508px;top:761px;width:592px;font-size:16px;line-height:21.5px;text-align:justify;color:#333}

/* focus */
.focus{position:absolute;top:1071px;left:0;width:1200px;height:502px;background:linear-gradient(90deg,#1a8a1a,#128812 40%,#0f800f)}
.focus-our{left:108px;top:50px;font-size:31px;color:var(--white);font-family:"Ubuntu",sans-serif}
.focus-title{left:108px;top:88px;font-size:37px;color:var(--white);font-family:"Ubuntu",sans-serif;font-weight:500}
.focus-text{left:108px;top:148px;width:330px;font-size:17.5px;line-height:30px;color:var(--white)}
.card{position:absolute;background:var(--white);padding:7px;text-align:center}
.card .photo{position:relative;height:200px}
.card h3{color:var(--green);font-size:21px;font-weight:700;margin-top:26px;line-height:30px}
.card p{font-size:17.5px;line-height:24px;color:#333;margin-top:10px;padding:0 20px}

/* services */
.h-section{left:0;width:1200px;text-align:center;font-family:"Ubuntu",sans-serif;font-weight:700;font-size:34px;letter-spacing:.5px}
.svc-title{font-family:"Ubuntu",sans-serif;font-size:38px;font-weight:500;color:#222}
.svc-text{font-size:19.5px;line-height:30px;color:#333}
.frame{position:absolute;border:3px solid var(--green)}

/* case studies */
.case{position:absolute;top:2643px;width:310px;height:450px;border:1px solid #e2e2e2;background:var(--white)}
.case.raised{box-shadow:0 0 12px rgba(0,0,0,.2)}
.case .photo{position:relative;height:214px}
.case-date{display:flex;align-items:center;gap:12px;margin:22px 0 0 17px;font-size:14.5px;color:#555;font-family:"Roboto",sans-serif}
.case-date .ic{width:12px;height:12px;border:2px solid var(--green);border-radius:50%}
.case h4{margin:18px 14px 0 17px;font-family:"Roboto",sans-serif;font-weight:500;font-size:18.5px;line-height:26px;color:#111;letter-spacing:-.1px}
.case p{margin:16px 17px 0;font-family:"Roboto",sans-serif;font-size:14.5px;line-height:26px;color:#555}
.case .more{display:inline-block;margin:14px 17px 0;font-family:"Roboto",sans-serif;font-size:15px;font-weight:500;color:#222;text-decoration:none;border-bottom:2px solid var(--green);line-height:18px}

/* footer */
.footer{position:absolute;top:3291px;left:0;width:1200px;height:401px;background:var(--footer);color:var(--white)}
.footer .brand-name{color:var(--white);font-size:22px}
.f-about{left:98px;top:176px;width:300px;font-size:15.5px;line-height:30px}
.f-head{font-size:20px;font-weight:700;font-family:"Ubuntu",sans-serif}
.f-links{left:448px;top:130px;list-style:none;font-size:15.5px;line-height:30px}
.f-contact{left:700px;font-size:15.5px;display:flex;gap:16px;align-items:flex-start;line-height:24px}
.f-soc{width:28px;height:28px;border-radius:4px;background:var(--white)}
.f-rule{left:97px;top:321px;width:1004px;height:1px;background:#777}
.copyright{left:0;top:343px;width:1200px;text-align:center;font-size:16.5px}
</style>
</head>
<body>

<!-- header -->
<header>
  <div class="brand" style="left:89px;top:30px">
    <span class="brand-dot"></span>
    <div class="brand-name">Veltrona5</div>
  </div>
  <nav class="nav">
    <a class="active" style="left:0">Home</a>
    <a style="left:72px">About Us</a>
    <a style="left:161px">What we do</a>
    <a style="left:277px">Areas of focus</a>
    <a style="left:410px">Blog</a>
    <a style="left:471px">Contact</a>
  </nav>
  <div class="phone">
    <svg width="16" height="16" viewBox="0 0 24 24"><path fill="#138a13" d="M6.6 10.8a15.1 15.1 0 0 0 6.6 6.6l2.2-2.2a1 1 0 0 1 1-.25 11.4 11.4 0 0 0 3.6.57 1 1 0 0 1 1 1V20a1 1 0 0 1-1 1A17 17 0 0 1 3 4a1 1 0 0 1 1-1h3.5a1 1 0 0 1 1 1c0 1.25.2 2.450.57 3.57a1 1 0 0 1-.25 1z"/></svg>
    +1 555 010 2040
  </div>
</header>

<!-- hero -->
<section class="hero">
  <div class="photo" style="inset:0" role="img" aria-label="Two food technologists in white coats and hairnets talking in a production facility"></div>
  <div class="hero-shade"></div>
  <h1 class="abs hero-title">WELCOME TO <b>VELTRONA5</b></h1>
  <p class="abs hero-text">Duis aute irure dolor in reprehenderit in voluptate velit esse cillum dolore eu fugiat nulla pariatur. Excepteur sint occaecat cupidatat non proident.</p>
  <a class="btn" style="left:103px;top:281px;width:171px;height:51px;font-size:17.5px">Get Started</a>
  <div class="abs follow">Follow Us <span class="rule"></span><span class="soc"></span><span class="soc"></span><span class="soc"></span></div>
</section>

<!-- about -->
<section>
  <svg class="abs" style="left:100px;top:640px" width="340" height="375" viewBox="0 0 340 375">
    <polygon points="170,8 330,98 330,278 170,368 10,278 10,98" fill="none" stroke="#138a13" stroke-width="10" transform="translate(-2,10)"/>
  </svg>
  <div class="photo" style="left:124px;top:634px;width:312px;height:377px;clip-path:polygon(50% 0,100% 24%,100% 76%,50% 100%,0 76%,0 24%);background:linear-gradient(160deg,#d8dcdf,#a9b2b8)" role="img" aria-label="Smiling technician in a hairnet and lab coat holding a tablet"></div>
  <div class="abs about-kicker">About Us</div>
  <h2 class="abs about-title">VELTRONA5</h2>
  <p class="abs about-text">Sed ut perspiciatis unde omnis iste natus error sit voluptatem accusantium doloremque laudantium, totam rem aperiam, eaque ipsa quae ab illo inventore veritatis et quasi architecto beatae vitae dicta sunt explicabo. Nemo enim ipsam voluptatem quia voluptas sit aspernatur aut odit aut fugit, sed quia consequuntur magni dolores eos qui ratione voluptatem sequi nesciunt. voluptatem. Ut enim ad minima veniam.</p>
  <a class="btn" style="left:500px;top:922px;width:149px;height:46px;font-size:15.5px">Read More</a>
</section>

<!-- areas of focus -->
<section class="focus">
  <div class="abs focus-our">Our</div>
  <h2 class="abs focus-title">Areas of focus</h2>
  <p class="abs focus-text">Sed ut perspiciatis unde omnis iste natus error sit voluptatem accusantium doloremque laudantium, totam rem aperiam, eaque ipsa quae ab illo inventore veritatis et quasi architecto beatae vitae dicta sunt explicabo.</p>
  <a class="btn btn-light" style="left:104px;top:366px;width:194px;height:52px;font-size:18.5px;font-weight:400">Show More</a>
  <div class="card" style="left:509px;top:52px;width:273px;height:414px">
    <div class="photo" style="background:linear-gradient(135deg,#6a2a8c,#c35fb5 50%,#e9d7ea)" role="img" aria-label="Two scientists inspecting plants under purple grow lights in a vertical farm"></div>
    <h3>Sustainable</h3>
    <p>Sed ut perspiciatis unde omnis iste natus error sit voluptatem accusantium doloremque laudantium, voluptas sit aspernatur.</p>
  </div>
  <div class="card" style="left:813px;top:52px;width:274px;height:414px">
    <div class="photo" style="background:linear-gradient(135deg,#6f8a3a,#a4b85a 45%,#d8c69a)" role="img" aria-label="Fresh greens, lemons and spices laid out on a table"></div>
    <h3>Fermentation-derived ingredients</h3>
    <p>Sed ut perspiciatis unde omnis iste natus error sit voluptatem accusantium doloremque</p>
  </div>
</section>

<!-- services -->
<section>
  <h2 class="abs h-section" style="top:1652px;color:var(--green)">OUR SERVICES</h2>

  <div class="frame" style="left:93px;top:1778px;width:208px;height:200px;border-right:none;border-bottom:none"></div>
  <div class="frame" style="left:312px;top:1872px;width:206px;height:203px;border-left:none;border-top:none"></div>
  <div class="photo" style="left:112px;top:1792px;width:388px;height:270px;background:linear-gradient(120deg,#4d4f52,#9ea3a6 50%,#d6d9db)" role="img" aria-label="Technician in a mask and gloves operating food processing machinery"></div>
  <h3 class="abs svc-title" style="left:604px;top:1776px">Food technology</h3>
  <p class="abs svc-text" style="left:604px;top:1839px;width:490px">Nemo enim ipsam voluptatem quia voluptas sit aspernatur aut odit aut fugit, sed quia consequuntur magni dolores eos qui ratione voluptatem sequi nesciunt. Neque porro quisquam est, qui dolorem ipsum quia dolor.</p>
  <a class="btn" style="left:607px;top:2016px;width:195px;height:59px;font-size:19.5px">Read More</a>

  <h3 class="abs svc-title" style="left:110px;top:2169px">Traditional companies</h3>
  <p class="abs svc-text" style="left:114px;top:2241px;width:490px">Nemo enim ipsam voluptatem quia voluptas sit aspernatur aut odit aut fugit, sed quia consequuntur magni dolores eos qui ratione voluptatem sequi nesciunt. Neque porro quisquam est, qui dolorem ipsum quia dolor.</p>
  <a class="btn" style="left:113px;top:2408px;width:195px;height:59px;font-size:19.5px">Read More</a>

  <div class="frame" style="left:662px;top:2178px;width:208px;height:200px;border-right:none;border-bottom:none"></div>
  <div class="frame" style="left:882px;top:2272px;width:205px;height:204px;border-left:none;border-top:none"></div>
  <div class="photo" style="left:681px;top:2192px;width:389px;height:270px;background:linear-gradient(135deg,#4b4a3c,#7b6a52 50%,#3d4a36)" role="img" aria-label="Overhead view of a shared table with plates of dishes and salads"></div>
</section>

<!-- case studies -->
<section>
  <h2 class="abs h-section" style="top:2557px;color:#222">CASE STUDIES</h2>

  <article class="case" style="left:112px">
    <div class="photo" style="background:linear-gradient(135deg,#5f7a4e,#b9c7b2 50%,#e3e8e4)" role="img" aria-label="Scientist in safety glasses working with plant samples in a laboratory"></div>
    <div class="case-date"><span class="ic"></span>April 04 , 2022</div>
    <h4>Sed ut perspiciatis unde omnis iste natus error sit voluptatem</h4>
    <p>Lorem ipsum dolor sit amet, consectetur adipiscing elit, sed do eiusmod tempor</p>
    <a class="more">Read More</a>
  </article>
  <article class="case raised" style="left:446px">
    <div class="photo" style="background:linear-gradient(135deg,#b9755a,#d9b38b 50%,#7aa24a)" role="img" aria-label="Worker in a hard hat carrying a crate of fresh vegetables"></div>
    <div class="case-date"><span class="ic"></span>April 04 , 2022</div>
    <h4>Nemo enim ipsam voluptatem quia voluptas sit</h4>
    <p>Lorem ipsum dolor sit amet, consectetur adipiscing elit, sed do eiusmod tempor</p>
    <a class="more">Read More</a>
  </article>
  <article class="case" style="left:779px">
    <div class="photo" style="background:linear-gradient(180deg,#9aa0a3 0%,#c6b48c 45%,#5f8a2c 65%,#3f7a1e 100%)" role="img" aria-label="Grain silos beside a green field at sunset"></div>
    <div class="case-date"><span class="ic"></span>April 04 , 2022</div>
    <h4>sed quia consequuntur magni dolores eos qui ratione</h4>
    <p>Lorem ipsum dolor sit amet, consectetur adipiscing elit, sed do eiusmod tempor</p>
    <a class="more">Read More</a>
  </article>

  <a class="btn" style="left:503px;top:3144px;width:194px;height:59px;font-size:19.5px">View articles.</a>
</section>

<!-- footer -->
<footer class="footer">
  <div class="brand" style="left:96px;top:92px;gap:10px">
    <span class="brand-dot" style="width:22px;height:22px"></span>
    <div class="brand-name">Veltrona5</div>
  </div>
  <p class="abs f-about">Sed ut perspiciatis unde omnis iste natus error sit volupta tem accusantium doloremque.</p>

  <div class="abs f-head" style="left:446px;top:74px">QUICK LINK</div>
  <ul class="abs f-links">
    <li>Home</li><li>About Us</li><li>What we do</li><li>Areas of focus</li><li>Blog</li><li>Contact</li>
  </ul>

  <div class="abs f-head" style="left:700px;top:72px">Contact</div>
  <div class="abs f-contact" style="top:130px">
    <svg width="14" height="20" viewBox="0 0 24 34" style="margin-top:3px"><path fill="#fff" d="M12 0a12 12 0 0 0-12 12c0 9 12 22 12 22s12-13 12-22A12 12 0 0 0 12 0zm0 17a5 5 0 1 1 0-10 5 5 0 0 1 0 10z"/></svg>
    <span>9904 Nemo enim ipsam<br>&nbsp;voluptatem quia</span>
  </div>
  <div class="abs f-contact" style="top:199px">
    <svg width="14" height="14" viewBox="0 0 24 24" style="margin-top:4px"><path fill="#fff" d="M6.6 10.8a15.1 15.1 0 0 0 6.6 6.6l2.2-2.2a1 1 0 0 1 1-.25 11.4 11.4 0 0 0 3.6.57 1 1 0 0 1 1 1V20a1 1 0 0 1-1 1A17 17 0 0 1 3 4a1 1 0 0 1 1-1h3.5a1 1 0 0 1 1 1c0 1.25.2 2.45.57 3.57a1 1 0 0 1-.25 1z"/></svg>
    <span>+1 555 010 2040</span>
  </div>
  <div class="abs f-contact" style="top:232px">
    <svg width="16" height="12" viewBox="0 0 24 18" style="margin-top:6px"><rect x="1" y="1" width="22" height="16" fill="none" stroke="#fff" stroke-width="2"/><path d="M1 1l11 9 11-9" fill="none" stroke="#fff" stroke-width="2"/></svg>
    <span>info@veltrona5.com</span>
  </div>

  <div class="abs f-head" style="left:968px;top:74px">Social with us</div>
  <div class="abs" style="left:970px;top:119px;display:flex;gap:20px">
    <span class="f-soc" aria-label="Social profile"></span><span class="f-soc" aria-label="Social profile"></span><span class="f-soc" aria-label="Social profile"></span>
  </div>

  <div class="abs f-rule"></div>
  <div class="abs copyright">© copyrights 2022 Veltrona5 |&nbsp; All Rights Reserved</div>
</footer>

</body>
</html>
```